Home page makeover

Take my existing home page, www.maplecrestledger.com and redesign layout to look more current considering today's touch design prevalence.
Reuse existing elements or suggest improved ones if available.
I generally have average CSS and HTML skills using div containers, defining lists and using columns to create the code to support the layout.
Updates
Just wanted to send out a quick message to thank all of you for your submissions. Many of you offered nice designs, but unfortunately could only choose one.
Target Market(s)
Generally targeting individuals with some assets for retirement. Basically your average working professional or business owner.
Industry/Entity Type
It Support
Look and feel
Each slider illustrates characteristics of the customer's brand and the style your logo design should communicate.

```html
<!DOCTYPE html>
<html lang="en">
<head>
<meta charset="utf-8">
<title>Maplecrest Ledger — Home</title>
<link rel="stylesheet" href="https://fonts.googleapis.com/css2?family=Open+Sans:ital,wght@0,300;0,400;0,600;0,700;1,300;1,400&display=swap">
<style>
:root{
  --green:#7fa63a;
  --green-dark:#5f8a25;
  --ink:#3a3a3a;
  --muted:#8a8a8a;
  --line:#dcdcdc;
  --footer:#3d3d47;
  --footer-text:#b9b9c2;
  --price-blue:#c9d6df;
  --bar:#40404a;
}
*{box-sizing:border-box;margin:0;padding:0}
html,body{width:835px;height:1200px;overflow:hidden;background:#fff}
body{position:relative;font-family:"Open Sans",Arial,sans-serif;color:var(--ink)}
.abs{position:absolute}

/* header */
.site-header{left:0;top:0;width:835px;height:67px;background:#fff;box-shadow:0 1px 3px rgba(0,0,0,.12);z-index:2}
.brand{left:36px;top:14px;display:flex;align-items:center;gap:8px}
.brand-mark{width:22px;height:22px;background:var(--green)}
.brand-name{font-size:17px;font-weight:700;color:var(--green);line-height:1}
.brand-tag{left:36px;top:45px;font-size:8px;color:var(--ink)}
.main-nav{left:307px;top:17px;width:226px;height:34px;background:#eeeeee;border-radius:4px;display:flex}
.main-nav a{flex:1;display:flex;align-items:center;justify-content:center;font-size:13px;color:#777;text-decoration:none;border-right:1px solid #dcdcdc}
.main-nav a:last-child{border-right:0}
.main-nav a.active{color:var(--green);font-weight:600}
.vdiv{width:1px;background:#e2e2e2}
.social-dot{width:9px;height:9px;border-radius:50%;background:#b5b5b5;top:32px}
.account-link{top:29px;font-size:10px;color:#9a9a9a;display:flex;align-items:center;gap:3px}
.account-link svg{width:10px;height:10px;fill:#b0b0b0}

/* hero */
.hero{left:0;top:67px;width:835px;height:348px;background:linear-gradient(100deg,#e9ebe6 0%,#f2f2f0 30%,#dcdcd8 55%,#c9cfd4 75%,#e3e6ea 100%)}
.hero-title{left:74px;top:198px;font-size:50px;font-weight:700;color:var(--green);letter-spacing:1px}
.slider-dot{top:380px;width:12px;height:12px;border-radius:50%;background:#d0d0d0;border:1px solid #bbb}
.slider-dot.active{background:var(--green);border-color:var(--green-dark)}

/* separators */
.sep{left:12px;width:811px;height:1px;background:var(--line)}
.sep-dots{left:421px;width:18px;display:flex;justify-content:space-between}
.sep-dots i{width:4px;height:4px;border-radius:50%;background:#c8c8c8}

/* pricing */
.price{top:466px;width:154px;height:122px;border:1px solid #d6d6d6;text-align:center;padding-top:10px}
.price-first{left:55px;background:#f7f7f7}
.price-second{left:212px;background:var(--price-blue);border-color:#aebdc9}
.price .only{font-size:20px;color:#555}
.price .amount{font-size:30px;font-weight:700;line-height:1.15}
.price-first .amount{color:var(--green)}
.price-second .amount{color:#333}
.price .term{font-size:11.5px;line-height:1.1;margin-top:8px}
.price-first .term{color:var(--green)}
.price-second .term{color:#555}
.signup-bar{left:55px;top:600px;width:311px;height:68px;background:var(--bar)}
.signup-btn{left:152px;top:614px;width:120px;height:41px;background:linear-gradient(#8ab842,#6b9a2a);border:1px solid #557d1f;border-radius:3px;color:#fff;font-size:14px;font-weight:600;display:flex;align-items:center;justify-content:center;gap:10px}

/* video */
.video{left:425px;top:449px;width:397px;height:229px;background:#000}
.video-progress{left:432px;top:647px;width:383px;height:3px;background:#cc1f1f}

/* features */
.section-title{font-size:26px;font-weight:400;color:var(--green);letter-spacing:.5px}
.feature-text{top:763px;width:378px;font-size:11.3px;line-height:1.5;color:#444}
.arrow-btn{top:716px;width:30px;height:30px;border:1px solid #cfcfcf;border-radius:2px;background:#fff;display:flex;align-items:center;justify-content:center}
.arrow-btn svg{width:10px;height:10px;stroke:#777;fill:none;stroke-width:1.6}

/* testimonials */
.subtitle{left:224px;top:872px;font-size:16px;color:#333;letter-spacing:.3px}
.subtitle b{font-weight:700}
.quote{left:28px;top:914px;font-size:18px;font-style:italic;font-weight:300;color:#444}
.quote .mark{font-size:30px;color:#b8b8b8;font-style:normal;vertical-align:-10px}
.author{left:497px;top:952px;font-size:12px;font-style:italic;color:#555}
.testimonial-photo{left:606px;top:854px;width:216px;height:120px;background:radial-gradient(ellipse at 55% 55%,#dcdfe2 0%,#eceeef 55%,#fff 80%)}
.pager{top:985px;display:flex;gap:4px;left:673px}
.pager span{width:17px;height:18px;border:1px solid #ccc;font-size:10px;display:flex;align-items:center;justify-content:center;color:#666}
.pager span.active{background:var(--green);border-color:var(--green);color:#fff}

/* footer */
.site-footer{left:0;top:1028px;width:835px;height:172px;background:var(--footer)}
.footer-brand{left:30px;top:1056px;display:flex;align-items:center;gap:7px}
.footer-brand .brand-name{color:#fff;font-size:15px}
.footer-brand .brand-mark{width:18px;height:18px}
.contact{left:30px;font-size:9.5px;color:var(--footer-text);display:flex;gap:6px;align-items:flex-start}
.contact svg{width:8px;height:9px;fill:var(--footer-text);margin-top:2px;flex:none}
.links-title{left:221px;top:1061px;font-size:13px;font-weight:600;color:#fff}
.links{left:218px;top:1084px;list-style:none;font-size:10px;color:var(--footer-text);line-height:1.2}
.links li::before{content:"> ";}
.footer-div{left:428px;top:1062px;width:1px;height:96px;background:#5c5c68}
.legal{left:449px;top:1062px;width:370px;font-size:9.4px;line-height:1.34;color:var(--footer-text);text-align:justify}
.copyright{right:16px;top:1174px;font-size:9.4px;color:var(--footer-text)}
</style>
</head>
<body>

<header class="site-header abs">
  <div class="brand abs"><span class="brand-mark"></span><span class="brand-name">Maplecrest Ledger</span></div>
  <div class="brand-tag abs">Plan Ahead Calmly</div>
  <nav class="main-nav abs">
    <a class="active">Home</a><a>About</a><a>Contact</a>
  </nav>
  <span class="vdiv abs" style="left:619px;top:14px;height:40px"></span>
  <span class="social-dot abs" style="left:632px"></span>
  <span class="social-dot abs" style="left:655px"></span>
  <span class="social-dot abs" style="left:676px"></span>
  <span class="vdiv abs" style="left:702px;top:14px;height:40px"></span>
  <span class="account-link abs" style="left:708px"><svg viewBox="0 0 10 10"><circle cx="5" cy="3" r="2.5"/><path d="M0 10a5 4 0 0 1 10 0z"/></svg>Login</span>
  <span class="vdiv abs" style="left:754px;top:14px;height:40px"></span>
  <span class="account-link abs" style="left:761px"><svg viewBox="0 0 10 10"><rect x="1" y="0" width="8" height="10" rx="1"/></svg>Signup</span>
</header>

<section class="hero abs" role="img" aria-label="Photo of hands holding a tablet showing banknotes, a pen and financial charts"></section>
<h1 class="hero-title abs">ITENTIFY</h1>
<span class="slider-dot active abs" style="left:540px"></span>
<span class="slider-dot abs" style="left:557px"></span>
<span class="slider-dot abs" style="left:574px"></span>

<div class="sep abs" style="top:426px"></div>
<div class="sep-dots abs" style="top:424px"><i></i><i></i><i></i></div>

<div class="price price-first abs">
  <div class="only">Only</div><div class="amount">$19.99</div>
  <div class="term">For a One Year<br>Membership</div>
</div>
<div class="price price-second abs">
  <div class="only">Only</div><div class="amount">$ 9.99</div>
  <div class="term">For a One Year<br>After that</div>
</div>
<div class="sep-dots abs" style="left:201px;top:593px"><i></i><i></i><i></i></div>
<div class="signup-bar abs"></div>
<div class="signup-btn abs">SIN UP <svg width="7" height="10" viewBox="0 0 7 10"><path d="M1 1l4 4-4 4" stroke="#fff" stroke-width="2" fill="none"/></svg></div>

<div class="video abs" role="img" aria-label="Embedded introduction video"></div>
<svg class="abs" style="left:597px;top:545px" width="52" height="36" viewBox="0 0 52 36">
  <circle cx="26" cy="18" r="17" fill="#3a3a3a"/><path d="M21 10l12 8-12 8z" fill="#fff"/>
</svg>
<div class="video-progress abs"></div>
<svg class="abs" style="left:438px;top:657px" width="60" height="12" viewBox="0 0 60 12">
  <path d="M0 1l9 5-9 5z" fill="#aaa"/><path d="M24 4h3l4-3v10l-4-3h-3z" fill="#aaa"/>
  <text x="42" y="10" font-size="8" fill="#aaa" font-family="Open Sans, sans-serif">0:00</text>
</svg>

<div class="sep abs" style="top:707px"></div>
<div class="sep-dots abs" style="top:705px"><i></i><i></i><i></i></div>

<h2 class="section-title abs" style="left:26px;top:718px">FEATURES</h2>
<div class="arrow-btn abs" style="left:763px"><svg viewBox="0 0 10 10"><path d="M7 1L3 5l4 4"/></svg></div>
<div class="arrow-btn abs" style="left:797px"><svg viewBox="0 0 10 10"><path d="M3 1l4 4-4 4"/></svg></div>
<p class="feature-text abs" style="left:26px">Identify and project your retirement needs and expectations including basic living expenses, housing costs, recreation, big ticket non-recurring items, medical and nursing home care.</p>
<span class="vdiv abs" style="left:428px;top:754px;height:72px"></span>
<p class="feature-text abs" style="left:443px">Strategize tapping into the equity of your real estate including swapping your primary residence for a different home or retirement area, or selling and renting.</p>

<div class="sep abs" style="top:848px"></div>
<div class="sep-dots abs" style="top:846px"><i></i><i></i><i></i></div>

<h2 class="section-title abs" style="left:26px;top:862px">TESTIMONIALS</h2>
<div class="subtitle abs">WHAT <b>PEOPLE SAY'S</b> ABOUT OUR WEBSITE</div>
<div class="testimonial-photo abs" role="img" aria-label="Photo of a customer behind a laptop giving a thumbs up"></div>
<p class="quote abs"><span class="mark">“</span> This site is a great place to get a handle on your retirement strategy <span class="mark">”</span></p>
<p class="author abs">Dana, Vermont</p>
<div class="pager abs"><span class="active">1</span><span>2</span><span>3</span></div>

<div class="sep abs" style="top:1014px"></div>
<div class="sep-dots abs" style="top:1012px"><i></i><i></i><i></i></div>

<footer class="site-footer abs"></footer>
<div class="footer-brand abs"><span class="brand-mark"></span><span class="brand-name">Maplecrest Ledger</span></div>
<div class="contact abs" style="top:1111px"><svg viewBox="0 0 8 10"><path d="M4 0a4 4 0 0 1 4 4c0 3-4 6-4 6S0 7 0 4a4 4 0 0 1 4-4z"/></svg><span>418 Alder Lane, Brookfield,<br>Portland, OR 97201-2044</span></div>
<div class="contact abs" style="top:1147px"><svg viewBox="0 0 8 10"><path d="M1 0h2l1 3-1.5 1a6 6 0 0 0 2.5 3L6 5.5l2 1V9l-1 1C3 10 0 6 0 1z"/></svg><span>1-555-010-2468</span></div>
<div class="contact abs" style="top:1165px"><svg viewBox="0 0 8 10"><rect x="2" y="0" width="4" height="3"/><rect x="0" y="3" width="8" height="4"/><rect x="2" y="6" width="4" height="4"/></svg><span>1-555-010-2468</span></div>

<div class="links-title abs">Links</div>
<ul class="links abs">
  <li>Home</li><li>About us</li><li>Contact us</li><li>Forget you passowrt</li><li>Registration</li>
</ul>
<span class="footer-div abs"></span>
<p class="legal abs">We'd like to hear from you if you have any questions or comments regarding the content of this web-site. Just click on Contact above. Copyright 2013, Maplecrest Ledger, Inc. All rights reserved. The "Nest Egg Gauge" is a Trademark of Maplecrest Ledger, Inc. All usage of this web-site is subject to the Terms and Conditions of Use you agreed to upon when accessing your user account. It should be duly noted that you will have no claim of any kind against Maplecrest Ledger, Inc. as a byproduct of using this web-site and gaining results from it, especially if you reside, are employed or have assets held outside of the United States.</p>
<p class="copyright abs">Copyright © 2013 maplecrestledger.com. All rights reserved. Terms of Use | Privacy Policy</p>

</body>
</html>
```